Web-page design

We need a initial web design for our page kavilora.com.au (which is not yet set up).
We provide consulting services for all kinds of problems in and between organisations.
Main focus is on conflict resolution but we also support companies on improving their operational performance.
We want to have the following page structure (and part of the project is to design the 8 pages):
- Home
- Services (we offer 3 main service areas - one per page)
- Case studies (one per page)
- Engaging us (our process)
- About Conflict & low performance
- Conflict resolution App
- About
- Contact (Email form)
- Our logo should be on each page.
The start page should include the following information:
- Twitter / Linkedin / facebook/ google + Links
- Telephone / Email or in general contact details
- News
- A quite prominent picture box with 3 alternating pics - each representing one of our service areas
- Link to our App
- Testimonials
It would be nice if the service pages would have an image header. Links to the information section (about conflict & low performance; and the app page) would be nice as well.
We like the following joomla designs: www.quorbixlane.com/itempreview/153
No need to copy it, it should just give you an idea.
We like the layout here with the picture and space for the case studies on the left. Somewhere beneath should be the 3 service areas with a picture each.
In terms of colors: our logo colours are Blue (RBG 8;44;80) and Orange (RGB 231;120;23). The orange could be used to emphasise certain things, however there should not be too much color.
Budget for images available, so please use placeholders or ask us for specific photos/images, if you need them for your design.
Updates
Hi, one more thing that we would like to have is the case studies not hidden behind a link "case studies" - we would like to have them individually linked prominent on the first page. There will be about 6-8 of them. Thats what we liked on the joomla template (the links left from the picture).
Hi, thanks very much for all the great proposals.
We are currently going through the selection process and will post our decision early next week.
Thanks again!
Liesel
Target Market(s)
- target customers are all different kinds of businesses and organisations (all industries, government, non-for-profit, ...) experiencing conflict and tension - be it with internal staff, amongst managers or board members, dysfunctional teams, between organizations or customers and organizations... examples could be bullying allegations, governmental negotiations with unions, disputes within organizations etc.
- also we will offer performance improvement services for organizations
- we will offer mediation, facilitation, negotiation, performance improvement services, conflict coaching, conflict management, change management services
- if comparable to anything - then to a law firm in terms of dealing with conflicts but its much less adversarial and much more about the people and their interests rather than about laws
- basically it's all kind of things you can do in order to solve disputes without involving lawyers and a court - so it's much cheaper and target is to find a solution all parties can live with rather than having a judge deciding about who wins and who looses
- performance management is more about analysing reasons for a lack of performance and setting up continous improvement systems, supporting change management, facilitating improvement workshops or strategic meetings, ...
Industry/Entity Type
Consulting
Look and feel

```html
<!DOCTYPE html>
<html lang="en">
<head>
<meta charset="utf-8">
<title>Marrow Tessel — Conflict Resolution &amp; Performance Consulting</title>
<link href="https://fonts.googleapis.com/css2?family=Roboto+Condensed:wght@400;700&family=Ubuntu:wght@300;400;500&display=swap" rel="stylesheet">
<style>
:root{
  --navy:#082c50;
  --navy-deep:#0a2a4a;
  --orange:#f28a30;
  --orange-deep:#e77817;
  --text:#6b6b6b;
  --muted:#9a9a9a;
  --line:#e6e6e6;
  --footer:#3a3a3a;
  --footer-bottom:#2c2c2c;
  --field:#5a5a5a;
  --white:#ffffff;
}
*{box-sizing:border-box;margin:0;padding:0}
html,body{width:1091px;height:1200px;overflow:hidden}
body{font-family:"Ubuntu",sans-serif;color:var(--text);background:var(--white);position:relative}
a{color:inherit;text-decoration:none}
ul{list-style:none}

/* top bar */
.topbar{height:27px;border-bottom:1px solid var(--line);background:#f7f7f7;display:flex;align-items:center;padding:0 0 0 74px;font-size:9px;color:var(--muted);position:relative}
.topbar .contact-item{display:flex;align-items:center;gap:4px;margin-right:12px}
.topbar .social{position:absolute;right:130px;top:8px;display:flex;gap:9px}
.dot{width:10px;height:10px;border-radius:50%;background:#b7b7b7;display:block}
.dot.active{background:var(--navy)}
.topbar .search{position:absolute;right:78px;top:0;width:28px;height:27px;border-left:1px solid var(--line);border-right:1px solid var(--line);display:flex;align-items:center;justify-content:center}

/* brand */
.brand{height:89px;text-align:center;padding-top:22px}
.brand-name{display:inline-flex;align-items:center;gap:12px;font-family:"Ubuntu",sans-serif;font-weight:400;font-size:26px;color:var(--navy);letter-spacing:.5px}
.brand-mark{width:14px;height:14px;border-radius:50%;background:var(--navy)}
.brand-url{font-size:10px;letter-spacing:7px;color:var(--navy);margin-top:8px}

/* nav */
.nav{height:37px;background:var(--navy-deep);border-bottom:2px solid var(--orange);display:flex;align-items:center;position:relative}
.nav-home{position:absolute;left:75px;top:0;width:63px;height:37px;background:var(--orange);display:flex;align-items:center;justify-content:center}
.nav-home span{width:14px;height:14px;border:2px solid var(--white)}
.nav-links{display:flex;margin-left:155px;font-family:"Roboto Condensed",sans-serif;font-weight:700;font-size:13px;color:var(--white);text-transform:uppercase}
.nav-links li{margin-right:29px;display:flex;align-items:center;gap:4px}
.caret{width:0;height:0;border-left:3.5px solid transparent;border-right:3.5px solid transparent;border-top:4px solid var(--white)}

/* hero */
.hero{position:relative;height:291px;overflow:hidden}
.hero-photo{position:absolute;inset:0;background:linear-gradient(180deg,#cfe2ef 0%,#e8eef0 45%,#d8c3ab 75%,#b99a80 100%)}
.case-panel{position:absolute;left:79px;top:26px;width:211px;background:rgba(235,235,235,.85)}
.case-panel h2{background:var(--navy);color:var(--white);font-family:"Roboto Condensed",sans-serif;font-weight:700;font-size:17px;letter-spacing:1px;height:40px;line-height:40px;padding-left:24px}
.case-panel li{height:25.2px;line-height:25px;border-bottom:1px solid #d2d2d2;font-size:11.5px;letter-spacing:.8px;color:#555;padding-left:40px;position:relative}
.case-panel li::before{content:"";position:absolute;left:26px;top:11px;border-top:3px solid transparent;border-bottom:3px solid transparent;border-left:4px solid #b5b5b5}
.case-panel li.current{background:var(--orange);color:var(--white)}
.case-panel li.current::before{border-left-color:var(--orange)}
.hero-copy{position:absolute;left:739px;top:76px}
.hero-copy h1{font-family:"Ubuntu",sans-serif;font-weight:400;font-size:27px;color:var(--navy);letter-spacing:.3px;margin-bottom:6px}
.hero-copy li{display:flex;align-items:center;gap:14px;font-size:12.5px;color:#666;height:27px}
.ring{width:19px;height:19px;border-radius:50%;border:2px solid var(--orange);display:flex;align-items:center;justify-content:center}
.ring i{width:7px;height:7px;border-radius:50%;background:var(--orange)}
.slide-arrow{position:absolute;top:119px;width:27px;height:27px;border-radius:50%;background:rgba(240,240,240,.9);display:flex;align-items:center;justify-content:center}
.slide-arrow.prev{left:17px}
.slide-arrow.next{right:51px}
.slide-dots{position:absolute;right:76px;top:270px;display:flex;gap:7px}
.slide-dots span{width:10px;height:10px;border-radius:50%;border:2px solid var(--white)}
.slide-dots span.on{border-color:var(--orange)}

/* app bar */
.app-bar{height:56px;background:var(--orange);display:flex;align-items:center;justify-content:center;color:var(--white);gap:8px}
.app-bar strong{font-weight:400;font-size:24px;letter-spacing:.3px}
.app-bar small{font-size:12px;margin-top:6px;margin-right:16px}
.app-bar .platforms{display:flex;gap:12px}
.app-bar .platforms span{width:16px;height:16px;border-radius:50%;background:var(--white)}
.app-shadow{height:22px;margin:0 70px;background:radial-gradient(ellipse at top,rgba(0,0,0,.12),rgba(0,0,0,0) 70%)}

/* content */
.content{position:absolute;top:551px;left:0;width:1091px;height:260px}
.service-card{position:absolute;top:0;width:211px}
.service-card .photo{height:103px;background:linear-gradient(135deg,#c9ccd1,#8b8f96 60%,#4a4e55)}
.service-card h3,.widget h3{font-family:"Roboto Condensed",sans-serif;font-weight:700;font-size:19px;color:var(--navy);margin:19px 0 6px}
.service-card p{font-size:11.5px;line-height:17.3px;text-align:justify}
.read-more{display:inline-block;margin-top:12px;color:var(--orange);font-size:12.5px;letter-spacing:.5px}
.read-more::after{content:" »";margin-left:4px}
.testimonials{position:absolute;left:811px;top:0;width:209px}
.testimonials h3{margin:0;display:inline-block;padding-bottom:2px;border-bottom:2px solid var(--orange)}
.quote{margin-top:23px;background:#9b9b9b;color:var(--white);font-style:italic;font-size:10px;line-height:15px;padding:11px 12px 20px 38px;position:relative}
.quote::before{content:"\201D\201D";position:absolute;left:12px;top:6px;font-size:26px;font-style:normal;letter-spacing:-4px}
.quote::after{content:"";position:absolute;left:0;bottom:-14px;border-top:14px solid #9b9b9b;border-right:14px solid transparent}
.author{display:flex;align-items:center;gap:10px;margin:16px 0 0 17px;font-size:11.5px;color:#444;line-height:17px}
.author .avatar{width:38px;height:38px;border-radius:50%;background:#cfd3d8;border:2px solid #eee}
.author small{color:#888;font-size:11px}

/* footer */
.footer{position:absolute;top:854px;left:0;width:1091px;height:288px;background:var(--footer);color:#bdbdbd}
.to-top{position:absolute;right:0;top:0;width:38px;height:34px;background:#2a2a2a;display:flex;align-items:center;justify-content:center}
.footer h4{font-family:"Roboto Condensed",sans-serif;font-weight:700;font-size:19px;color:var(--white);display:inline-block;padding-bottom:1px;border-bottom:2px solid var(--orange);margin-bottom:14px}
.footer-col{position:absolute;top:36px}
.quick-links li{font-size:11.5px;height:23.8px;padding-left:18px;position:relative}
.quick-links li::before{content:"";position:absolute;left:0;top:5px;border-top:3px solid transparent;border-bottom:3px solid transparent;border-left:4px solid #999}
.about-us p{font-size:11.5px;line-height:14.6px;text-align:justify;letter-spacing:.3px;margin-bottom:14px;color:#b0b0b0}
.about-us .read-more{margin-top:0}
.contact-form .field{width:209px;height:26px;background:var(--field);margin-bottom:9px;font-size:12px;color:#c8c8c8;padding:6px 12px}
.contact-form .field.message{height:73px}
.contact-form .send{margin:2px 0 0 146px;width:63px;height:26px;background:var(--orange);color:var(--white);font-family:"Roboto Condensed",sans-serif;font-weight:700;font-size:14px;display:flex;align-items:center;justify-content:center}
.footer-bottom{position:absolute;top:1142px;left:0;width:1091px;height:58px;background:var(--footer-bottom);border-top:1px solid #555;display:flex;align-items:center;padding-left:70px;color:#c4c4c4;font-size:12.5px;letter-spacing:.4px}
.footer-bottom .mark{width:14px;height:14px;border:2px solid #aaa;margin-right:14px}
.footer-bottom .social{position:absolute;right:184px;display:flex;gap:16px}
.footer-bottom .social span{width:16px;height:16px;border-radius:50%;background:#8a8a8a}
</style>
</head>
<body>

<header>
  <div class="topbar">
    <span class="contact-item">
      <svg width="10" height="10" viewBox="0 0 10 10"><path d="M2 1l2 2-1 1.3c.6 1.2 1.5 2.1 2.7 2.7L7 6l2 2-1.3 1.3C4.5 9 1 5.5.7 2.3z" fill="#aaa"/></svg>
      +1 800 555-0148
    </span>
    <span class="contact-item">
      <svg width="11" height="8" viewBox="0 0 11 8"><rect width="11" height="8" fill="#aaa"/><path d="M0 0l5.5 4.5L11 0" stroke="#f7f7f7" fill="none"/></svg>
      contact@kavilora.com.au
    </span>
    <div class="social"><span class="dot active"></span><span class="dot"></span><span class="dot"></span><span class="dot"></span></div>
    <div class="search"><svg width="11" height="11" viewBox="0 0 11 11"><circle cx="4.5" cy="4.5" r="3.3" stroke="#f28a30" stroke-width="1.6" fill="none"/><path d="M7 7l3 3" stroke="#f28a30" stroke-width="2"/></svg></div>
  </div>

  <div class="brand">
    <div class="brand-name"><span class="brand-mark"></span><span>MARROW TESSEL</span></div>
    <div class="brand-url">www.kavilora.com.au</div>
  </div>

  <nav class="nav">
    <a class="nav-home" href="#"><span></span></a>
    <ul class="nav-links">
      <li>Services <i class="caret"></i></li>
      <li>Case Studies <i class="caret"></i></li>
      <li>Engaging Us</li>
      <li>About Conflict &amp; Low Performance</li>
      <li>Conflict Resolution App</li>
      <li>About</li>
      <li>Contact</li>
    </ul>
  </nav>
</header>

<section class="hero">
  <div class="hero-photo" role="img" aria-label="Businessman in white shirt and tie stretching his arms wide against a blurred sky and mountain backdrop"></div>
  <div class="case-panel">
    <h2>CASE STUDIES</h2>
    <ul>
      <li>Managing Services</li>
      <li>Consulting Services</li>
      <li class="current">Policy Analysis</li>
      <li>Market Assessment</li>
      <li>Program Management</li>
      <li>Regulatory Support</li>
      <li>Risk Assessment</li>
      <li>Market Research</li>
    </ul>
  </div>
  <div class="hero-copy">
    <h1>LOREM IPSUM DOLOR</h1>
    <ul>
      <li><span class="ring"><i></i></span>Sed ut eros ac diam dapibus commodo</li>
      <li><span class="ring"><i></i></span>Sed ut eros ac diam dapibus</li>
      <li><span class="ring"><i></i></span>Sed ut eros ac diam</li>
    </ul>
  </div>
  <a class="slide-arrow prev" href="#"><svg width="8" height="10" viewBox="0 0 8 10"><path d="M6 1L2 5l4 4" stroke="#888" stroke-width="2" fill="none"/></svg></a>
  <a class="slide-arrow next" href="#"><svg width="8" height="10" viewBox="0 0 8 10"><path d="M2 1l4 4-4 4" stroke="#f28a30" stroke-width="2" fill="none"/></svg></a>
  <div class="slide-dots"><span class="on"></span><span></span><span></span></div>
</section>

<section class="app-bar">
  <strong>Download our app.</strong>
  <small>Signup to get future news and updates</small>
  <div class="platforms"><span></span><span></span><span></span></div>
</section>
<div class="app-shadow"></div>

<main class="content">
  <article class="service-card" style="left:70px">
    <div class="photo" role="img" aria-label="Team of business people in an office, one pointing forward"></div>
    <h3>ETIAM ALIQUET SAPIEN</h3>
    <p>Amet neque iaculis viverra. In tincidunt neque eget ipsum mollis, sed placerat lectus iaculis. Donec ut orci ultrices sem hendrerit volutpat in sit amet odio. Etiam ut mattis orci.</p>
    <a class="read-more" href="#">Read more</a>
  </article>
  <article class="service-card" style="left:317px">
    <div class="photo" role="img" aria-label="Smiling businesswoman in front of colleagues"></div>
    <h3>ETIAM ALIQUET SAPIEN</h3>
    <p>Amet neque iaculis viverra. In tincidunt neque eget ipsum mollis, sed placerat lectus iaculis. Donec ut orci ultrices sem hendrerit volutpat in sit amet odio. Etiam ut mattis orci.</p>
    <a class="read-more" href="#">Read more</a>
  </article>
  <article class="service-card" style="left:561px">
    <div class="photo" role="img" aria-label="Senior businessman in suit and tie in an office"></div>
    <h3>ETIAM ALIQUET SAPIEN</h3>
    <p>Amet neque iaculis viverra. In tincidunt neque eget ipsum mollis, sed placerat lectus iaculis. Donec ut orci ultrices sem hendrerit volutpat in sit amet odio. Etiam ut mattis orci.</p>
    <a class="read-more" href="#">Read more</a>
  </article>

  <aside class="testimonials widget">
    <h3>TESTIMONIALS</h3>
    <blockquote class="quote">orem ipsum dolor sit amet, consectetur adipisicing elit, sed do eiusmod tempor incididunt labore et dolore magna aliqua. Ut enim ad minim veniam.</blockquote>
    <div class="author">
      <span class="avatar" role="img" aria-label="Portrait of the client"></span>
      <div>Oren Valdtke<br><small>Manager</small></div>
    </div>
    <a class="read-more" href="#" style="margin-top:26px">All testimonials</a>
  </aside>
</main>

<footer class="footer">
  <a class="to-top" href="#"><svg width="12" height="8" viewBox="0 0 12 8"><path d="M1 7l5-5 5 5" stroke="#999" stroke-width="1.5" fill="none"/></svg></a>

  <div class="footer-col" style="left:70px">
    <h4>QUICK LINK</h4>
    <ul class="quick-links">
      <li>Services</li>
      <li>Case Studies</li>
      <li>Engaging Us</li>
      <li>About Conflict &amp; Low Performance</li>
      <li>Conflict Resolution App</li>
      <li>About</li>
      <li>Contact</li>
    </ul>
  </div>

  <div class="footer-col about-us" style="left:317px;width:455px">
    <h4>ABOUT US</h4>
    <p>Donec sagittis aliquet accumsan. Vivamus vitae mauris ullamcorper, suscipit erat nec, cursus lectus. Nullam a blandit dui, ac convallis lacus. Ut in tellus dictum, venenatis eros imperdiet, faucibus libero. Proin euismod purus non risus facilisis, lobortis fringilla sapien pulvinar. Nulla sollicitudin tellus vel gravida pharetra. Curabitur sed dolor at nulla sodales sollicitudin a quis lorem. Nulla imperdiet vitae libero a sodales. Fusce faucibus tortor auctor ante scelerisque luctus.</p>
    <p>Nam pharetra turpis et augue varius, eget accumsan dui vulputate. Praesent ac orci sodales quam pulvinar lacinia eget ac ligula.</p>
    <a class="read-more" href="#">Read more</a>
  </div>

  <form class="footer-col contact-form" style="left:811px">
    <h4>CONTACT FORM</h4>
    <div class="field">Your Name:*</div>
    <div class="field">Your Email:*</div>
    <div class="field message">Your Message:*</div>
    <div class="send">SEND</div>
  </form>
</footer>

<div class="footer-bottom">
  <span class="mark"></span>
  Copyright © 2013&nbsp; All Rights Reserved.
  <div class="social"><span></span><span></span><span></span><span></span></div>
</div>

</body>
</html>
```